Re-design of website

I have an existing website that I would like to improve. The functionality will remain the same but the overall look will need to be changed. I have some ideas of what i would like included and am also in need of someone else to input their own creative ideas. I am on a tight deadline to get these improvements made as I have many people being directed to the site via our advertising campaigns that are in full swing late next week. Thanks
Target Market(s)
The website provides a virtual space for families to learn more about our learning program which we operate out of Dubai and will soon spread to the other Emirates. The families are generally between 25-50 year old parents with children up to the age of 6. They are local Emirati's as well as expats.
Look and feel

```html
<!DOCTYPE html>
<html lang="en">
<head>
<meta charset="utf-8">
<title>Little Summit – Accelerated Learning Centre</title>
<link href="https://fonts.googleapis.com/css2?family=Play:wght@400;700&family=Roboto:wght@300;400&display=swap" rel="stylesheet">
<style>
:root{
  --blue:#5b8fa8;
  --blue-light:#19b4ea;
  --navy:#3c5a8c;
  --orange:#f39a3d;
  --orange-deep:#ff6b35;
  --grey-card:#9a9a9a;
  --text-dark:#3a3a3a;
  --header-bg:#f4f4f4;
  --white:#fff;
}
*{box-sizing:border-box;margin:0;padding:0}
html,body{width:950px;height:1200px;overflow:hidden}
body{font-family:"Roboto",Arial,sans-serif;color:var(--text-dark);position:relative;
  background:linear-gradient(#fff 0,#fff 458px,#f2f2f2 470px,#fff 700px);}
.header-bg{position:absolute;left:0;top:0;width:950px;height:458px;background:var(--header-bg)}
.band-top{position:absolute;top:0;left:0;width:950px;height:20px;background:var(--blue)}
.band-bottom{position:absolute;bottom:0;left:0;width:950px;height:28px;background:var(--orange)}
.abs{position:absolute}
.brand{left:63px;top:50px;width:151px;height:132px;display:flex;flex-direction:column;align-items:center;justify-content:center;gap:10px}
.brand-dot{width:62px;height:62px;border-radius:50%;background:var(--blue)}
.brand-name{font-family:"Play",sans-serif;font-weight:700;font-size:22px;color:var(--blue)}
.brand-tag{left:64px;top:190px;width:150px;height:45px;background:var(--blue);border-radius:7px;color:#fff;
  font-family:"Play",sans-serif;font-weight:700;font-size:12.5px;line-height:14px;text-align:center;display:flex;align-items:center;justify-content:center}
.mascots{left:338px;top:44px;width:250px;height:198px;border-radius:14px;
  background:linear-gradient(160deg,#f3c978,#8cbfd2 55%,#e9a0ad)}
.register{left:594px;top:14px;width:110px;height:110px;border-radius:50%;background:var(--orange);
  color:#fff;font-family:"Play",sans-serif;font-weight:700;font-size:17px;line-height:18.5px;text-align:center;display:flex;align-items:center;justify-content:center}
.go{left:692px;top:37px;width:64px;height:64px;border-radius:50%;background:#fff;border:2px solid var(--orange);
  text-align:center;font-family:"Play",sans-serif;font-weight:700;font-size:16px;color:#555;padding-top:8px}
.go svg{display:block;margin:2px auto 0}
.hotline{left:680px;top:122px;width:200px;text-align:center;font-family:"Play",sans-serif}
.hotline .label{font-size:15.5px;color:#555}
.hotline .number{font-size:17px;color:#999;margin-top:3px;letter-spacing:.5px}
.ribbon{top:181px;width:44px;height:52px}
.nav{left:51px;top:251px}
.nav a{position:absolute;top:0;height:34px;border:1.5px solid #e0e0e0;border-radius:17px;background:#fff;
  font-family:"Play",sans-serif;font-weight:700;font-size:14px;color:#777;text-decoration:none;display:flex;align-items:center;justify-content:center}
.nav a.active{background:var(--orange);border-color:var(--orange);color:#fff}
.hero{left:51px;top:296px;width:846px;height:345px;border:1px solid #ddd;background:#fff;box-shadow:0 8px 10px -8px rgba(0,0,0,.2)}
.hero-photo{position:absolute;left:0;top:0;width:594px;height:343px;background:linear-gradient(120deg,#e9d6c4,#f7efe6 50%,#d9c2aa)}
.dots{position:absolute;left:292px;top:320px;display:flex;gap:7px}
.dots span{width:10px;height:10px;border-radius:50%;background:#888}
.dots span.on{background:#444}
.hero-panel{position:absolute;left:594px;top:0;width:250px;height:343px;background:var(--orange)}
.hero-kid{position:absolute;left:42px;top:28px;width:58px;height:125px;border-radius:28px;background:linear-gradient(#d98a4b,#3b6fa8)}
.hero-badge{position:absolute;left:107px;top:39px;width:110px;height:110px;border-radius:50%;background:#3a3a3a}
.hero-text{position:absolute;left:15px;top:174px;width:222px;text-align:center;color:#fff;font-family:"Play",sans-serif;font-size:20.5px;line-height:22.8px}
.card{top:687px;width:276px;height:386px;color:#fff;padding:0 16px}
.card h2{font-family:"Play",sans-serif;font-weight:400;font-size:23px;padding:12px 4px 5px;border-bottom:1px solid rgba(255,255,255,.7);margin-bottom:15px}
.card .frame{background:#fff;padding:8px;border-radius:4px;height:146px}
.card .frame div{width:100%;height:100%}
.card p{font-size:11.4px;font-weight:300;line-height:14.8px;padding:12px 6px 0}
.card p+p{padding-top:14px}
.more{position:absolute;right:16px;bottom:12px;width:68px;height:23px;background:#fff;color:#333;font-size:11px;text-decoration:underline;display:flex;align-items:center;justify-content:center}
.company{left:51px;background:var(--grey-card)}
.program{left:336px;background:var(--orange-deep)}
.media{left:621px;background:var(--orange)}
.video{height:178px;background:linear-gradient(#2a2a2a,#5a4a4a 60%,#1a1a1a);position:relative}
.video .play{position:absolute;left:107px;top:74px;width:34px;height:30px;border-radius:6px;background:rgba(0,0,0,.6)}
.video .play:after{content:"";position:absolute;left:13px;top:8px;border-left:11px solid #fff;border-top:7px solid transparent;border-bottom:7px solid transparent}
.video .bar{position:absolute;left:0;bottom:0;width:100%;height:16px;background:#111}
.video .title{position:absolute;left:7px;top:5px;font-size:8px;color:#fff}
.footer-line{left:23px;top:1087px;width:900px;height:1px;background:#bbb}
.footer-nav{left:0;top:1106px;width:950px;text-align:center;font-family:"Play",sans-serif;font-weight:700;font-size:14px;color:#333}
.copyright{left:0;top:1128px;width:950px;text-align:center;font-size:10.5px;color:#555}
</style>
</head>
<body>
<div class="header-bg"></div>
<div class="band-top"></div>

<div class="abs brand"><span class="brand-dot"></span><span class="brand-name">Little Summit</span></div>
<div class="abs brand-tag">Accelerated Learning<br>Centre</div>

<div class="abs mascots" role="img" aria-label="Illustration of two cheerful school children walking hand in hand with backpacks"></div>

<div class="abs register">Register<br>your<br>interest<br>today!</div>
<div class="abs go">Go
  <svg width="22" height="20" viewBox="0 0 22 20"><path d="M2 7h10V1l9 9-9 9v-6H2z" fill="#3c72c4"/></svg>
</div>

<div class="abs hotline"><div class="label">Hotline phone number</div><div class="number">+971 500 000 123</div></div>

<svg class="abs ribbon" style="left:734px" viewBox="0 0 44 52"><path d="M0 0h44v52L22 40 0 52z" fill="var(--navy)"/></svg>
<svg class="abs ribbon" style="left:786px" viewBox="0 0 44 52"><path d="M0 0h44v52L22 40 0 52z" fill="var(--blue-light)"/></svg>

<nav class="abs nav">
  <a class="active" style="left:0;width:86px">Home</a>
  <a style="left:93px;width:112px">Our Method</a>
  <a style="left:209px;width:120px">The Program</a>
  <a style="left:335px;width:87px">Media</a>
  <a style="left:426px;width:94px">Locations</a>
  <a style="left:524px;width:93px">About Us</a>
  <a style="left:621px;width:102px">Contact Us</a>
  <a style="left:727px;width:119px">News &amp; Events</a>
</nav>

<section class="abs hero">
  <div class="hero-photo" role="img" aria-label="Photo of a smiling mother lying with her young daughter and son"></div>
  <div class="dots"><span></span><span class="on"></span><span></span><span></span></div>
  <div class="hero-panel">
    <div class="hero-kid" role="img" aria-label="Illustration of a boy with a backpack"></div>
    <div class="hero-badge" role="img" aria-label="Brain icon"></div>
    <div class="hero-text">The brain develops almost entirely between the age 0 to 6 years old. Let us help your child to be the best they can be!</div>
  </div>
</section>

<section class="abs card company">
  <h2>Our Company</h2>
  <div class="frame"><div role="img" aria-label="Photo of a mother playing with building blocks with her baby" style="background:linear-gradient(120deg,#c99a6e,#efe2d2)"></div></div>
  <p>Little Summit Accelerated Learning Centre is the first a whole brain training program designed to maximise your child's potential during this key period of development.</p>
  <a class="more">more info</a>
</section>

<section class="abs card program">
  <h2>The Program</h2>
  <div class="frame"><div role="img" aria-label="Photo of a toddler playing with an abacus and learning cards" style="background:linear-gradient(120deg,#e2c28c,#e4e4e4 45%,#8fa3bd)"></div></div>
  <p>Our preschool program and accelerated learning activities are for the early learner age group 6 months to 6 years old.</p>
  <p>We currently offer the program in English.</p>
  <p>Our classes are 50 minutes and we request a parent or carer to attend the class with the child.</p>
  <a class="more">more info</a>
</section>

<section class="abs card media">
  <h2>Media</h2>
  <div class="video" role="img" aria-label="Video still of a speech on early childhood education in front of an audience">
    <span class="title">Speech on Early Childhood Education</span>
    <span class="play"></span><span class="bar"></span>
  </div>
  <p style="padding-top:20px">Governor Elena Marsh urging citizens to encourage learning at the earliest possible age in a child's life. "Study after study shows that the earlier a child begins learning the better he or she does down the road"</p>
  <a class="more">more info</a>
</section>

<div class="abs footer-line"></div>
<div class="abs footer-nav">Home | Our Method | The Program | Media | Locations | About Us | Contact Us | News &amp; Events</div>
<div class="abs copyright">©2013 Little Summit, All rights reserved.</div>

<div class="band-bottom"></div>
</body>
</html>
```